Meal Prep website

Website needed for local meal prep service. Simple template to start off with and then looking to be able to take orders from members

Target Market(s)

Toronto area fitness professionals, athletes and people looking for become healthier

Industry/Entity Type

It Service

Number of Pages Required

5+ page

Font styles to use
Sans Serif

Colors
000000

Requirements
Must have
• Landing page giving information about who we are and what type of service we provide.
• Links to social media. Plattorbowls on Instagram
Nice to have
• E-commerce section allowing users to select and place orders while accepting payments

```html
<!DOCTYPE html>
<html lang="en">
<head>
<meta charset="utf-8">
<title>Plattorbowls – Meal Delivery Service</title>
<link href="https://fonts.googleapis.com/css2?family=Nunito+Sans:ital,wght@0,400;0,600;0,700;0,800;0,900;1,400&family=Open+Sans:ital,wght@0,400;0,600;1,400&display=swap" rel="stylesheet">
<style>
  :root{
    --green:#3b7a3f;
    --green-dark:#2f6634;
    --lime:#9cc51e;
    --white:#ffffff;
    --black:#0d0d0d;
    --ink:#141414;
    --muted:#cfd8cf;
    --footer-text:#d6d6d6;
    --line:#3a3a3a;
  }
  *{box-sizing:border-box;margin:0;padding:0}
  html,body{width:1200px;height:3025px;overflow:hidden}
  body{position:relative;background:var(--black);font-family:"Open Sans",Arial,sans-serif;color:var(--white)}
  .abs{position:absolute}
  .heading{font-family:"Nunito Sans",Arial,sans-serif;font-weight:800;text-align:center;left:0;width:1200px;font-size:35px;letter-spacing:.5px}
  .leaf{position:absolute;left:582px;width:36px;height:30px}

  /* hero */
  .hero{top:0;left:0;width:1200px;height:537px;
    background:radial-gradient(ellipse at 62% 55%,#7a4a2a 0%,#4a3a22 25%,#2a2a26 55%,#1c1c1c 100%)}
  .hero-shade{top:0;left:0;width:1200px;height:537px;background:linear-gradient(#000a,#0003 40%,#0006)}
  .brand{top:38px;left:100px;font-family:"Nunito Sans",sans-serif;font-weight:900;font-size:34px;color:var(--lime)}
  .phone{top:16px;left:712px;display:flex;align-items:center;gap:10px;font-family:"Nunito Sans",sans-serif;font-weight:700;font-size:17px}
  .phone-ring{width:32px;height:32px;border:2px solid var(--lime);border-radius:50%;display:flex;align-items:center;justify-content:center}
  .order-online{top:15px;left:902px;width:148px;height:34px;border:2px solid var(--lime);border-radius:17px;font-family:"Nunito Sans",sans-serif;font-weight:800;font-size:14px;color:var(--lime);display:flex;align-items:center;justify-content:center}
  .social-square{top:14px;left:1061px;width:36px;height:36px;border-radius:6px;background:#2a7ab8;border:2px solid #fff}
  .nav{top:64px;left:545px;display:flex;gap:24px;font-family:"Nunito Sans",sans-serif;font-weight:700;font-size:17px}
  .nav .active{color:var(--lime)}
  .search{top:68px;left:1085px}
  .hero-title{top:150px;left:0;width:1200px;text-align:center;font-family:"Nunito Sans",sans-serif;font-weight:800;font-size:64px;letter-spacing:10px}
  .hero-sub{top:240px;left:0;width:1200px;text-align:center;font-family:"Nunito Sans",sans-serif;font-weight:600;font-size:22px}
  .signup{top:298px;left:343px;display:flex}
  .signup .field{width:369px;height:47px;background:#fff;color:#999;font-size:12px;padding:0 26px;display:flex;align-items:center}
  .signup .go{width:146px;height:47px;background:var(--lime);font-family:"Nunito Sans",sans-serif;font-weight:800;font-size:15px;display:flex;align-items:center;justify-content:center}
  .dots{display:flex;gap:6px}
  .dot{width:14px;height:14px;border-radius:50%;border:2px solid #fff}
  .dot.on{background:#fff}

  /* who we are */
  .who{top:537px;left:0;width:1200px;height:433px;background:var(--green)}
  .who-text{top:178px;left:216px;width:800px;text-align:center;font-size:13.5px;line-height:32px;color:var(--muted)}
  .outline-btn{border:2px solid var(--lime);color:var(--lime);font-family:"Nunito Sans",sans-serif;font-weight:800;display:flex;align-items:center;justify-content:center}
  .about-btn{top:324px;left:516px;width:168px;height:46px;border-radius:23px;font-size:15px}

  /* services */
  .services{top:970px;left:0;width:1200px;height:480px;
    background:radial-gradient(ellipse at 60% 70%,#5a3e2a 0%,#3a2c22 35%,#1d1a17 100%)}
  .services-shade{top:0;left:0;width:1200px;height:480px;background:#0008}
  .step-label{width:240px;text-align:center;font-family:"Nunito Sans",sans-serif;font-weight:700;font-size:20px;line-height:35px}

  /* meals */
  .meals{top:1450px;left:0;width:1200px;height:642px;background:var(--green)}
  .meal{position:absolute;top:184px;width:316px}
  .meal-photo{width:316px;height:217px;border:3px solid #fff;position:relative}
  .price{position:absolute;right:0;bottom:0;background:#1b1b1b;font-family:"Nunito Sans",sans-serif;font-weight:700;font-size:18px;padding:6px 14px}
  .meal-title{margin-top:32px;font-family:"Nunito Sans",sans-serif;font-weight:700;font-size:19px}
  .meal-desc{margin-top:12px;font-size:12.5px;line-height:25px;color:var(--muted)}
  .order-btn{margin-top:14px;width:135px;height:38px;border-radius:19px;font-size:14px}
  .arrow-btn{top:1719px;width:44px;height:44px;border-radius:50%;background:#2a5a2d;display:flex;align-items:center;justify-content:center}

  /* reviews */
  .reviews{top:2092px;left:0;width:1200px;height:560px;
    background:radial-gradient(ellipse at 55% 75%,#4e6a2c 0%,#35401f 35%,#141414 80%)}
  .reviews-shade{top:0;left:0;width:1200px;height:560px;background:#0007}
  .avatar{top:182px;left:542px;width:114px;height:114px;border-radius:50%;border:4px solid #fff;background:linear-gradient(#7a8ea0,#5a6270)}
  .quote{top:324px;left:280px;width:640px;text-align:center;font-style:italic;font-size:14px;line-height:32px;color:#e6e6e6}
  .author{top:428px;left:0;width:1200px;text-align:center;font-family:"Nunito Sans",sans-serif;font-weight:700;font-size:17px}

  /* footer */
  .footer-col{top:2715px}
  .footer-col h4{font-family:"Nunito Sans",sans-serif;font-weight:700;font-size:18px;margin-bottom:12px}
  .footer-col ul{list-style:none;font-size:11.5px;line-height:27.5px;color:var(--footer-text)}
  .divider{top:2715px;width:1px;height:200px;background:var(--line)}
  .sub-note{font-size:11.5px;color:var(--footer-text);margin-bottom:10px}
  .sub-form{display:flex}
  .sub-form .field{width:230px;height:35px;background:#fff}
  .sub-form .go{width:93px;height:35px;background:var(--lime);font-family:"Nunito Sans",sans-serif;font-weight:800;font-size:12px;display:flex;align-items:center;justify-content:center}
  .socials{display:flex;gap:6px;margin-top:10px}
  .socials span{width:36px;height:36px;border-radius:50%;border:2px solid #fff}
  .copyright{top:2946px;left:0;width:1200px;border-top:1px solid var(--line);padding-top:22px;text-align:center;font-size:11.5px;color:var(--footer-text)}
</style>
</head>
<body>

<!-- HERO -->
<section class="abs hero" role="img" aria-label="Photo of grilled chicken with roasted peppers and onions in a pan on dark slate"></section>
<div class="abs hero-shade"></div>
<div class="abs brand">Plattorbowls</div>
<div class="abs phone">
  <span class="phone-ring">
    <svg width="14" height="14" viewBox="0 0 24 24"><path d="M6.6 10.8a15 15 0 0 0 6.6 6.6l2.2-2.2c.3-.3.7-.4 1-.2 1.1.4 2.3.6 3.6.6.6 0 1 .4 1 1V20c0 .6-.4 1-1 1A17 17 0 0 1 3 4c0-.6.4-1 1-1h3.5c.6 0 1 .4 1 1 0 1.3.2 2.5.6 3.6.1.3 0 .7-.2 1z" fill="#9cc51e"/></svg>
  </span>
  1 555 010 2040
</div>
<div class="abs order-online">ORDER ONLINE</div>
<div class="abs social-square"></div>
<nav class="abs nav">
  <span class="active">Home</span><span>About</span><span>Services</span><span>Our Packages</span><span>Locations</span><span>Contact</span>
</nav>
<svg class="abs search" width="18" height="18" viewBox="0 0 24 24"><circle cx="10" cy="10" r="7" fill="none" stroke="#fff" stroke-width="3"/><line x1="15" y1="15" x2="22" y2="22" stroke="#fff" stroke-width="3"/></svg>
<h1 class="abs hero-title">PLATTORBOWLS</h1>
<p class="abs hero-sub">Plattorbowls Meals Biweekly Meal Delivery Service</p>
<div class="abs signup"><div class="field">Email Address</div><div class="go">VIEW PLANS</div></div>
<div class="abs dots" style="top:471px;left:562px"><span class="dot on"></span><span class="dot"></span><span class="dot"></span><span class="dot"></span></div>

<!-- WHO WE ARE -->
<section class="abs who">
  <svg class="leaf" style="top:60px" role="img" aria-label="leaf mark" viewBox="0 0 36 30"><ellipse cx="18" cy="15" rx="12" ry="9" fill="#9cc51e"/></svg>
  <h2 class="abs heading" style="top:104px">WHO WE ARE</h2>
  <p class="abs who-text">At vero eos et accusamus et iusto odio dignissimos ducimus qui blanditiis praesentium voluptatum deleniti atque corrupti quos dolores et quas molestias excepturi sint occaecati cupiditate non provident, similique sunt in culpa qui officia deserunt mollitia animi, id est laborum et dolorum fuga. Et harum quidem rerum facilis est et expedita distinctio. Nam libero tempore, cum soluta nobis est eligendi optio cumque nihil impedit quo minus id quod maxime placeat facere.</p>
  <div class="abs outline-btn about-btn">ABOUT US</div>
</section>

<!-- SERVICES -->
<section class="abs services" role="img" aria-label="Photo of a fresh salad plate with fork on a wooden table"></section>
<div class="abs services-shade" style="top:970px"></div>
<svg class="leaf" style="top:1020px" role="img" aria-label="leaf mark" viewBox="0 0 36 30"><ellipse cx="18" cy="15" rx="12" ry="9" fill="#9cc51e"/></svg>
<h2 class="abs heading" style="top:1060px">SERVICES WE PROVIDE</h2>
<svg class="abs" style="top:1140px;left:0" width="1200" height="190" viewBox="0 0 1200 190">
  <g fill="none" stroke="#fff">
    <line x1="328" y1="94" x2="512" y2="94" stroke-width="2"/>
    <line x1="685" y1="94" x2="873" y2="94" stroke-width="2"/>
    <polyline points="410,84 420,94 410,104" stroke-width="4"/>
    <polyline points="767,84 777,94 767,104" stroke-width="4"/>
    <circle cx="242" cy="94" r="86" stroke-width="2"/>
    <circle cx="599" cy="94" r="86" stroke-width="2"/>
    <circle cx="960" cy="94" r="86" stroke-width="2"/>
  </g>
  <g fill="#0a0a0a" stroke="#fff" stroke-width="3">
    <circle cx="242" cy="94" r="76"/><circle cx="599" cy="94" r="76"/><circle cx="960" cy="94" r="76"/>
  </g>
  <!-- cloche -->
  <g fill="#9cc51e">
    <circle cx="242" cy="60" r="6"/>
    <path d="M202 106 A40 40 0 0 1 282 106 Z"/>
    <rect x="194" y="110" width="96" height="8" rx="3"/>
  </g>
  <!-- truck -->
  <g fill="#9cc51e">
    <rect x="560" y="70" width="50" height="40" rx="3"/>
    <path d="M614 82 h20 l12 16 v12 h-32 z"/>
    <circle cx="575" cy="116" r="8" stroke="#0a0a0a" stroke-width="3"/>
    <circle cx="628" cy="116" r="8" stroke="#0a0a0a" stroke-width="3"/>
  </g>
  <!-- smiley -->
  <g fill="none" stroke="#9cc51e" stroke-width="5">
    <circle cx="960" cy="94" r="32"/>
    <path d="M943 102 q17 18 34 0" stroke-linecap="round"/>
  </g>
  <g fill="#9cc51e"><circle cx="948" cy="84" r="4.5"/><circle cx="972" cy="84" r="4.5"/></g>
</svg>
<div class="abs step-label" style="top:1333px;left:122px">Choose your<br>Plan and Meals</div>
<div class="abs step-label" style="top:1333px;left:479px">We Cook &amp;<br>Deliver</div>
<div class="abs step-label" style="top:1333px;left:840px">Enjoy your<br>Meals</div>

<!-- MEALS -->
<section class="abs meals">
  <svg class="leaf" style="top:46px" role="img" aria-label="leaf mark" viewBox="0 0 36 30"><ellipse cx="18" cy="15" rx="12" ry="9" fill="#9cc51e"/></svg>
  <h2 class="abs heading" style="top:94px">OUR MEALS</h2>

  <article class="meal" style="left:99px">
    <div class="meal-photo" role="img" aria-label="Photo of a meal prep container with rice, vegetables and stew" style="background:linear-gradient(135deg,#d8d2c4,#6a4a32 55%,#2a2622)"><span class="price">$25.00</span></div>
    <h3 class="meal-title">Finibus Bonorum et Malorum</h3>
    <p class="meal-desc">At vero eos et accusamus et iusto odio dignissimos ducimus qui blanditiis praesentiu.</p>
    <div class="outline-btn order-btn">ORDER NOW!</div>
  </article>
  <article class="meal" style="left:442px">
    <div class="meal-photo" role="img" aria-label="Photo of a salad bowl with greens, rice and tomatoes" style="background:linear-gradient(135deg,#6a9a34,#d8c448 50%,#b84a2a)"><span class="price">$25.00</span></div>
    <h3 class="meal-title">Finibus Bonorum et Malorum</h3>
    <p class="meal-desc">At vero eos et accusamus et iusto odio dignissimos ducimus qui blanditiis praesentiu.</p>
    <div class="outline-btn order-btn">ORDER NOW!</div>
  </article>
  <article class="meal" style="left:785px">
    <div class="meal-photo" role="img" aria-label="Photo of boxed salads with beans, corn and greens" style="background:linear-gradient(135deg,#c8a25a,#d6c234 45%,#3a5a2a)"><span class="price">$25.00</span></div>
    <h3 class="meal-title">Finibus Bonorum et Malorum</h3>
    <p class="meal-desc">At vero eos et accusamus et iusto odio dignissimos ducimus qui blanditiis praesentiu.</p>
    <div class="outline-btn order-btn">ORDER NOW!</div>
  </article>
</section>
<div class="abs arrow-btn" style="left:44px"><svg width="14" height="14" viewBox="0 0 14 14"><polyline points="9,2 4,7 9,12" fill="none" stroke="#fff" stroke-width="2"/></svg></div>
<div class="abs arrow-btn" style="left:1111px"><svg width="14" height="14" viewBox="0 0 14 14"><polyline points="5,2 10,7 5,12" fill="none" stroke="#fff" stroke-width="2"/></svg></div>

<!-- REVIEWS -->
<section class="abs reviews" role="img" aria-label="Photo of a green salad with tomatoes being dressed with oil"></section>
<div class="abs reviews-shade" style="top:2092px"></div>
<div style="position:absolute;top:2092px;left:0;width:1200px;height:560px">
  <svg class="leaf" style="top:54px" role="img" aria-label="leaf mark" viewBox="0 0 36 30"><ellipse cx="18" cy="15" rx="12" ry="9" fill="#9cc51e"/></svg>
  <h2 class="abs heading" style="top:100px">CUSTOMER REVIEWS</h2>
  <div class="abs avatar" role="img" aria-label="Portrait photo of the reviewer"></div>
  <p class="abs quote">“ Nam libero tempore, cum soluta nobis est eligendi optio cumque nihil impedit quo minus id quod maxime placeat facere possimus, omnis voluptas assumenda est, omnis dolor repellen bus autem quibusdam et aut officiis debitis aut rerum necessitatibus saepe eveniet ”</p>
  <p class="abs author">- JOHN DOE</p>
  <div class="abs dots" style="top:479px;left:578px"><span class="dot on"></span><span class="dot"></span><span class="dot"></span></div>
</div>
<svg class="abs" style="top:2560px;left:0" width="1200" height="100" viewBox="0 0 1200 100">
  <path d="M0 60 Q600 130 1200 60 L1200 100 L0 100 Z" fill="#0d0d0d"/>
  <path d="M30 14 Q600 150 1170 14 Q600 118 30 14 Z" fill="#9cc51e"/>
</svg>

<!-- FOOTER -->
<div class="abs footer-col" style="left:100px">
  <h4>Information</h4>
  <ul><li>About Us</li><li>Careers</li><li>Privacy &amp; Security</li><li>Site Map</li><li>Terms of Use</li><li>Blog</li></ul>
</div>
<div class="abs divider" style="left:258px"></div>
<div class="abs footer-col" style="left:303px">
  <h4>Help &amp; support</h4>
  <ul><li>Recommended Reading</li><li>Submit your Story</li><li>Contact Us</li><li>Frequently Asked Questions</li><li>How to Order</li></ul>
</div>
<div class="abs divider" style="left:506px"></div>
<div class="abs footer-col" style="left:551px">
  <h4>My Account</h4>
  <ul><li>Delivery Information</li><li>My Account</li><li>Order Tracking</li><li>Reminder Service</li><li>Shipping, Returns &amp; Fees</li></ul>
</div>
<div class="abs divider" style="left:733px"></div>
<div class="abs footer-col" style="left:778px">
  <h4>Email Subscription</h4>
  <p class="sub-note">Register your email address to get information about us</p>
  <div class="sub-form"><div class="field"></div><div class="go">SUBSCRIBE</div></div>
  <h4 style="margin-top:14px;margin-bottom:0">Stay Connected</h4>
  <div class="socials">
    <span style="background:#3b5a98"></span><span style="background:#2fa6e0"></span><span style="background:#d9453a"></span><span style="background:#3a6f9a"></span>
  </div>
</div>
<div class="abs copyright">Copyrights © 2017, Plattorbowls. All Rights Reserved &nbsp;|&nbsp; Privacy Policy | Terms of Use | Feedback</div>

</body>
</html>
```